Koveli Seafood Shipping Packaging Re-Design

We need a packaging (Shipping Carton) design for our Seafood Products (FROZEN). We already have a basic packaging design which we prefer to have a modern touch on it.
Spec :
1. It must show our logo (Attached), note that the text of "KOVELI" which accompany the logo is optional, it can be omitted & showing only the logo.
2. Main color is Blue
3. Our carton is regular shipping box with dimension L43cm x W 27cm x H 16cm.
4. Our material of Carton is both Brown & White Kraft Paperboard, so the design should look nice in both material.

Attached our Logo and packaging design.

Target Market(s)

Frozen Seafood Distributor & Seafood Buyer

Industry/Entity Type

Food Production

Requirements
Must have
• 1. Must Show our Logo
• 2. Main Color of the Text/Logo is Blue
• 3. On the side of the packaging / Carton must show two box of CODE & SIZE
• 4. Must Show these icons :
• a. Handle with Care
• b. Maximum Stackable 10 Carton
• c. Recyleable Material
• d. Protect from the Water/Rain
Nice to have
• Would prefer to have a modern design

```html
<!DOCTYPE html>
<html lang="en">
<head>
<meta charset="utf-8">
<title>Koveli Frozen Fish Shipping Carton</title>
<link href="https://fonts.googleapis.com/css2?family=Josefin+Sans:wght@300;400&family=Montserrat:wght@500;600&family=Cormorant+Garamond:wght@600&family=Noto+Serif+SC:wght@500&display=swap" rel="stylesheet">
<style>
  :root {
    --bg: #e4e5e7;
    --navy: #1f3a8a;
    --navy-deep: #1a2f78;
    --aqua-light: #a9e2e4;
    --aqua: #6dd0e0;
    --cyan: #25bcd8;
    --white: #ffffff;
    --ice: #dff4f8;
  }
  * { margin: 0; padding: 0; box-sizing: border-box; }
  html, body { width: 1200px; height: 1200px; overflow: hidden; background: var(--bg); }
  .sheet {
    position: relative; width: 1200px; height: 1200px;
    display: flex; flex-direction: column; align-items: center; justify-content: center; gap: 36px;
  }
  .panel {
    position: relative; overflow: hidden;
    background: linear-gradient(100deg, var(--aqua-light) 0%, var(--aqua) 55%, var(--cyan) 100%);
    box-shadow: 0 10px 30px rgba(0,0,0,0.12);
  }
  .panel--top { width: 1000px; height: 250px; }
  .panel--long { width: 1000px; height: 372px; }
  .panel--end { width: 700px; height: 320px; }

  /* brand block */
  .brand {
    position: absolute; left: 48px; top: 36px; width: 300px;
    display: flex; flex-direction: column; align-items: flex-start;
  }
  .brand__mark { display: flex; align-items: center; gap: 10px; }
  .brand__dot { width: 32px; height: 32px; border-radius: 50%; background: var(--navy); }
  .brand__name {
    font-family: "Josefin Sans", sans-serif; font-weight: 400; font-size: 28px;
    letter-spacing: 4px; color: var(--navy); line-height: 1;
  }
  .brand__product {
    margin-top: 30px;
    font-family: "Josefin Sans", sans-serif; font-weight: 300; font-size: 60px; line-height: 0.95;
    color: var(--navy); letter-spacing: 2px;
  }
  .brand__product span { display: block; padding-left: 30px; }

  .panel--top .brand { top: 24px; }
  .panel--top .brand__dot { width: 24px; height: 24px; }
  .panel--top .brand__name { font-size: 22px; }
  .panel--top .brand__product { margin-top: 14px; font-size: 44px; }

  .product-photo {
    position: absolute;
    background: radial-gradient(ellipse at 50% 48%, #6e6a4a 0%, #8f8a66 28%, var(--ice) 62%, rgba(223,244,248,0) 76%);
  }
  .panel--long .product-photo { left: 400px; top: 24px; width: 400px; height: 270px; }
  .panel--top .product-photo { left: 340px; top: 10px; width: 480px; height: 170px; }

  .temp { position: absolute; }
  .panel--long .temp { right: 60px; top: 40px; }
  .panel--top .temp { right: 60px; top: 36px; }

  /* notice band */
  .band {
    position: absolute; left: 0; right: 0; bottom: 0; height: 70px;
    border-top: 6px solid var(--navy); background: var(--navy-deep);
    display: flex; align-items: center; justify-content: space-around; padding: 0 30px;
  }
  .panel--top .band { height: 56px; }
  .panel--end .band { justify-content: space-between; padding: 0 26px; }
  .notice { display: flex; align-items: center; gap: 10px; color: var(--white);
    font-family: "Montserrat", sans-serif; font-weight: 500; font-size: 13px; line-height: 1.2; white-space: nowrap; }
  .notice svg { flex: none; }
  .panel--top .notice, .panel--end .notice { font-size: 12px; gap: 8px; }

  /* code & size fields */
  .fields { position: absolute; left: 70px; right: 70px; top: 34px; display: flex; gap: 70px; }
  .field { flex: 1; height: 200px; border: 2px solid var(--navy); display: flex; flex-direction: column; }
  .field__label {
    height: 52px; border-bottom: 2px solid var(--navy);
    display: flex; align-items: center; justify-content: center;
    font-family: "Cormorant Garamond", "Noto Serif SC", serif; font-weight: 600; font-size: 30px;
    letter-spacing: 4px; color: var(--navy);
  }
  .field__label .cjk { font-family: "Noto Serif SC", serif; font-size: 24px; letter-spacing: 2px; }
</style>
</head>
<body>
<main class="sheet">

  <section class="panel panel--top" aria-label="Carton top flaps">
    <div class="brand">
      <div class="brand__mark">
        <span class="brand__dot"></span>
        <span class="brand__name">KOVELI</span>
      </div>
      <h2 class="brand__product">FROZEN<span>FISH</span></h2>
    </div>

    <div class="product-photo" role="img" aria-label="Photograph of a whole bass lying on crushed ice cubes"></div>

    <svg class="temp" width="56" height="120" viewBox="0 0 70 150" aria-label="Keep frozen at minus 18 degrees">
      <g stroke="var(--navy)" stroke-width="3" fill="none" stroke-linecap="round">
        <line x1="14" y1="6" x2="14" y2="38"/><line x1="0" y1="22" x2="28" y2="22"/>
        <line x1="4" y1="12" x2="24" y2="32"/><line x1="24" y1="12" x2="4" y2="32"/>
        <path d="M42 14 a8 8 0 0 1 16 0 v96 a14 14 0 1 1 -16 0 z"/>
      </g>
      <circle cx="50" cy="122" r="8" fill="var(--navy)"/>
      <line x1="50" y1="40" x2="50" y2="116" stroke="var(--navy)" stroke-width="4"/>
      <text x="6" y="62" font-family="Montserrat, sans-serif" font-size="16" font-weight="600" fill="var(--navy)">-18</text>
    </svg>

    <div class="band">
      <div class="notice">
        <svg width="24" height="24" viewBox="0 0 30 30" fill="none" stroke="#fff" stroke-width="2"><rect x="9" y="3" width="12" height="12"/><path d="M3 16 q4 10 12 10 q8 0 12 -10"/></svg>
        <span>FROZEN</span>
      </div>
      <div class="notice">
        <svg width="22" height="26" viewBox="0 0 26 30" fill="#fff"><text x="2" y="13" font-family="Montserrat, sans-serif" font-size="13" font-weight="600">10</text><rect x="2" y="17" width="22" height="3"/><rect x="2" y="23" width="22" height="3"/></svg>
        <span>Maximum Stackable<br>10 Carton</span>
      </div>
      <div class="notice">
        <svg width="24" height="24" viewBox="0 0 30 30" fill="none" stroke="#fff" stroke-width="2.5"><path d="M15 4 L25 20 H5 Z"/><path d="M11 20 l-3 -3 M19 20 l3 -3"/></svg>
        <span>Recyleable Material</span>
      </div>
      <div class="notice">
        <svg width="20" height="24" viewBox="0 0 24 30"><path d="M12 3 C12 3 3 15 3 20 a9 9 0 0 0 18 0 C21 15 12 3 12 3 Z" fill="#fff"/></svg>
        <span>Protect from<br>The Water/Rain</span>
      </div>
    </div>
  </section>

  <section class="panel panel--long" aria-label="Carton long side">
    <div class="brand">
      <div class="brand__mark">
        <span class="brand__dot"></span>
        <span class="brand__name">KOVELI</span>
      </div>
      <h1 class="brand__product">FROZEN<span>FISH</span></h1>
    </div>

    <div class="product-photo" role="img" aria-label="Photograph of a whole bass leaping from crushed ice cubes"></div>

    <svg class="temp" width="70" height="150" viewBox="0 0 70 150" aria-label="Keep frozen at minus 18 degrees">
      <g stroke="var(--navy)" stroke-width="3" fill="none" stroke-linecap="round">
        <line x1="14" y1="6" x2="14" y2="38"/><line x1="0" y1="22" x2="28" y2="22"/>
        <line x1="4" y1="12" x2="24" y2="32"/><line x1="24" y1="12" x2="4" y2="32"/>
        <path d="M42 14 a8 8 0 0 1 16 0 v96 a14 14 0 1 1 -16 0 z"/>
      </g>
      <circle cx="50" cy="122" r="8" fill="var(--navy)"/>
      <line x1="50" y1="40" x2="50" y2="116" stroke="var(--navy)" stroke-width="4"/>
      <text x="6" y="62" font-family="Montserrat, sans-serif" font-size="16" font-weight="600" fill="var(--navy)">-18</text>
    </svg>

    <div class="band">
      <div class="notice">
        <svg width="30" height="30" viewBox="0 0 30 30" fill="none" stroke="#fff" stroke-width="2"><rect x="9" y="3" width="12" height="12"/><path d="M3 16 q4 10 12 10 q8 0 12 -10"/></svg>
        <span>FROZEN</span>
      </div>
      <div class="notice">
        <svg width="26" height="30" viewBox="0 0 26 30" fill="#fff"><text x="2" y="13" font-family="Montserrat, sans-serif" font-size="13" font-weight="600">10</text><rect x="2" y="17" width="22" height="3"/><rect x="2" y="23" width="22" height="3"/></svg>
        <span>Maximum Stackable<br>10 Carton</span>
      </div>
      <div class="notice">
        <svg width="30" height="30" viewBox="0 0 30 30" fill="none" stroke="#fff" stroke-width="2.5"><path d="M15 4 L25 20 H5 Z"/><path d="M11 20 l-3 -3 M19 20 l3 -3"/></svg>
        <span>Recyleable Material</span>
      </div>
      <div class="notice">
        <svg width="24" height="30" viewBox="0 0 24 30"><path d="M12 3 C12 3 3 15 3 20 a9 9 0 0 0 18 0 C21 15 12 3 12 3 Z" fill="#fff"/></svg>
        <span>Protect from<br>The Water/Rain</span>
      </div>
    </div>
  </section>

  <section class="panel panel--end" aria-label="Carton end side">
    <div class="fields">
      <div class="field"><div class="field__label">CODE/<span class="cjk">代码</span></div></div>
      <div class="field"><div class="field__label">SIZE/<span class="cjk">规格</span></div></div>
    </div>
    <div class="band">
      <div class="notice">
        <svg width="24" height="24" viewBox="0 0 30 30" fill="none" stroke="#fff" stroke-width="2"><rect x="9" y="3" width="12" height="12"/><path d="M3 16 q4 10 12 10 q8 0 12 -10"/></svg>
        <span>FROZEN</span>
      </div>
      <div class="notice">
        <svg width="22" height="26" viewBox="0 0 26 30" fill="#fff"><text x="2" y="13" font-family="Montserrat, sans-serif" font-size="13" font-weight="600">10</text><rect x="2" y="17" width="22" height="3"/><rect x="2" y="23" width="22" height="3"/></svg>
        <span>Maximum Stackable<br>10 Carton</span>
      </div>
      <div class="notice">
        <svg width="24" height="24" viewBox="0 0 30 30" fill="none" stroke="#fff" stroke-width="2.5"><path d="M15 4 L25 20 H5 Z"/><path d="M11 20 l-3 -3 M19 20 l3 -3"/></svg>
        <span>Recyleable Material</span>
      </div>
      <div class="notice">
        <svg width="20" height="24" viewBox="0 0 24 30"><path d="M12 3 C12 3 3 15 3 20 a9 9 0 0 0 18 0 C21 15 12 3 12 3 Z" fill="#fff"/></svg>
        <span>Protect from<br>The Water/Rain</span>
      </div>
    </div>
  </section>

</main>
</body>
</html>
```